Packaging design for a reclosable bag for our product

We have a logo, and we need to put it on packaging for our product and while we want the look to be simple, we want it to follow good design principles and also contain spaces for other product descriptions.

There will be 5 sizes at launch so I'd like 5 variations, one for each size.

I've included a few mockups of the type of bag that I made but they are all just rough ideas that I had.

I want the brand to look scientific and methodical and even a bit quirky, as in "wow this is a serious product but also a bit unusual."

```html
<!DOCTYPE html>
<html lang="en">
<head>
<meta charset="utf-8">
<title>KR4 Bias Lighting – 5m Pouch</title>
<link href="https://fonts.googleapis.com/css2?family=Open+Sans:wght@600&family=Roboto+Condensed:wght@400;700&display=swap" rel="stylesheet">
<style>
  :root {
    --backdrop: #9c9ca0;
    --pouch-light: #ececec;
    --pouch-dark: #222222;
    --zip-light: #d8d8d8;
    --zip-dark: #111111;
    --size-grey: #555555;
    --label-grey: #b8b8b8;
    --ink-white: #f2f2f2;
  }
  * { margin: 0; padding: 0; box-sizing: border-box; }
  html, body {
    width: 1023px;
    height: 1200px;
    overflow: hidden;
    background: var(--backdrop);
  }
  .canvas {
    position: relative;
    width: 1023px;
    height: 1200px;
  }
  .pouch {
    position: absolute;
    left: 231px;
    top: 120px;
    width: 560px;
    height: 960px;
    overflow: hidden;
  }
  .pouch-art {
    position: absolute;
    inset: 0;
  }
  .size-figure {
    position: absolute;
    left: 382px;
    top: 258px;
    font-family: "Roboto Condensed", sans-serif;
    font-weight: 700;
    font-size: 84px;
    line-height: 1;
    color: var(--size-grey);
    letter-spacing: -1px;
  }
  .size-label {
    position: absolute;
    left: 384px;
    top: 344px;
    font-family: "Roboto Condensed", sans-serif;
    font-weight: 400;
    font-size: 23px;
    line-height: 1;
    color: var(--label-grey);
  }
  .brand-name {
    position: absolute;
    left: 166px;
    top: 415px;
    font-family: "Open Sans", sans-serif;
    font-weight: 600;
    font-size: 185px;
    line-height: 1;
    color: var(--ink-white);
    letter-spacing: -7px;
    white-space: nowrap;
  }
  .product-name {
    position: absolute;
    left: 168px;
    top: 598px;
    font-family: "Open Sans", sans-serif;
    font-weight: 600;
    font-size: 53px;
    line-height: 1;
    color: var(--ink-white);
    letter-spacing: -0.5px;
    white-space: nowrap;
  }
  .spec-lines {
    position: absolute;
    left: 172px;
    top: 699px;
    font-family: "Roboto Condensed", sans-serif;
    font-weight: 400;
    font-size: 31px;
    line-height: 40px;
    color: var(--ink-white);
    white-space: nowrap;
  }
  .spec-lines strong { font-weight: 700; }
</style>
</head>
<body>
  <main class="canvas">
    <section class="pouch" aria-label="5m Extra Large bias lighting pouch">
      <svg class="pouch-art" width="560" height="960" viewBox="0 0 560 960" aria-hidden="true">
        <defs>
          <linearGradient id="lightPanel" x1="0" y1="0" x2="1" y2="1">
            <stop offset="0" stop-color="#f4f4f4"/>
            <stop offset="1" stop-color="#e2e2e2"/>
          </linearGradient>
          <linearGradient id="darkPanel" x1="0" y1="0" x2="0" y2="1">
            <stop offset="0" stop-color="#1c1c1c"/>
            <stop offset="1" stop-color="#2c2c2c"/>
          </linearGradient>
        </defs>
        <rect class="panel-dark" x="0" y="0" width="560" height="960" fill="url(#darkPanel)"/>
        <polygon class="panel-light" points="0,0 455,0 0,632" fill="url(#lightPanel)"/>
        <line class="zip-seal" x1="44" y1="105" x2="528" y2="113" stroke="var(--zip-light)" stroke-width="3"/>
        <line class="zip-seal" x1="44" y1="112" x2="528" y2="120" stroke="var(--zip-light)" stroke-width="2"/>
        <line class="zip-seal-dark" x1="380" y1="110" x2="528" y2="113" stroke="var(--zip-dark)" stroke-width="3"/>
        <line class="zip-seal-dark" x1="370" y1="117" x2="528" y2="120" stroke="var(--zip-dark)" stroke-width="2"/>
        <circle class="tear-notch" cx="0" cy="56" r="6" fill="var(--backdrop)"/>
        <circle class="tear-notch" cx="560" cy="72" r="6" fill="var(--backdrop)"/>
      </svg>
      <p class="size-figure">5m</p>
      <p class="size-label">Extra Large</p>
      <h1 class="brand-name">KR4</h1>
      <h2 class="product-name">Bias Lighting</h2>
      <p class="spec-lines">Simulated <strong>D65 CRI90+</strong><br><strong>6500K</strong> White Bias Lighting</p>
    </section>
  </main>
</body>
</html>
```